New Public Cloud Consulting Needs Powerpoint Template

Setting up a new consulting practice and need a powerpoint template and design that reflects our vision. We focus on KRT Public Cloud only. We want to emphasize innovation, cloud, speed. We are based in Asia, with headquarters in Singapore. We serve Asia and Europe customers. The attached file is the current template and logo that we use. However it is not dynamic enough. Blue is the color of our logo - but we must have other colors that complement the blue.

Target Market(s)

Innovation, cloud, advisory

Font styles to use
Other font styles liked:
• We want a different font that what is included in the file.

Requirements
Must have
• Logo which is included in the sample template and blue color - however we want other colors included. To date - most of the designs are completely blue - which we do not want. Additionally we need to create an image of innovation, future vision. Please do not include a picture of a cloud. That is not innovative.
Nice to have
• Would be nice to show people in some of the slides - professional etc. There is one slide in the attached presentation that gives you an idea of this concept. How else can we do this ?

```html
<!DOCTYPE html>
<html lang="en">
<head>
<meta charset="utf-8">
<title>NOVA Consulting Group – Slide Template</title>
<link href="https://fonts.googleapis.com/css2?family=Poppins:wght@300;400;600;700&display=swap" rel="stylesheet">
<style>
  :root {
    --board: #e6e6e6;
    --blue: #3a63b0;
    --blue-deep: #2c4f95;
    --blue-navy: #1f3a7a;
    --blue-soft: #7391c9;
    --blue-pale: #a9bce0;
    --panel-grey: #f3f4f7;
    --line-grey: #b9bcc4;
    --white: #ffffff;
    --pale-tri: #eef0f8;
    --orange: #e07b45;
  }
  * { box-sizing: border-box; margin: 0; padding: 0; }
  html, body { width: 1200px; height: 1153px; overflow: hidden; background: var(--board); font-family: "Poppins", sans-serif; }
  .board { position: relative; width: 1200px; height: 1153px; }
  .slide { position: absolute; width: 536px; height: 301px; background: var(--white); overflow: hidden; box-shadow: 0 3px 6px rgba(0,0,0,.22); }
  .slide > svg.shapes { position: absolute; inset: 0; }
  .slide--hero { left: 335px; top: 79px; }
  .slide--cover { left: 53px; top: 423px; }
  .slide--topics { left: 618px; top: 423px; }
  .slide--focus { left: 53px; top: 772px; }
  .slide--services { left: 618px; top: 772px; background: var(--blue); }
  .abs { position: absolute; }
  .brand { position: absolute; font-weight: 600; color: var(--blue-navy); line-height: 1; white-space: nowrap; }
  .brand--large { font-size: 25px; }
  .brand--large small { display: block; font-size: 9px; margin-top: 2px; font-weight: 600; }
  .brand--small { font-size: 10px; }
  .brand--small small { display: block; font-size: 4px; font-weight: 600; }
  .headline { color: var(--white); font-weight: 300; font-size: 15px; line-height: 1.12; }
  .rule { position: absolute; height: 1.5px; background: var(--white); }
  .strong-line { color: var(--white); font-weight: 700; font-size: 14px; }
  .slide-title { position: absolute; left: 26px; top: 12px; font-size: 16px; font-weight: 300; color: var(--blue); letter-spacing: .2px; }
  .slide--services .slide-title { color: var(--white); }
  .topic { position: absolute; width: 80px; height: 38px; background: var(--blue); color: var(--white); font-size: 10px; font-weight: 700; line-height: 1.15; display: flex; align-items: center; justify-content: center; text-align: center; box-shadow: 0 2px 3px rgba(0,0,0,.2); }
  .topic-icon { position: absolute; width: 20px; height: 20px; border-radius: 50%; background: var(--blue-deep); border: 1.5px solid var(--white); left: 30px; top: -11px; }
  .point { position: absolute; width: 82px; font-size: 8px; font-weight: 700; color: var(--blue); line-height: 1.2; }
  .service { position: absolute; font-size: 9.5px; font-weight: 700; color: var(--white); line-height: 1.15; white-space: nowrap; }
  .service--left { text-align: right; }
  .pill { position: absolute; left: 463px; top: 269px; width: 73px; height: 22px; background: var(--white); border-radius: 11px 0 0 11px; }
</style>
</head>
<body>
<main class="board">

  <!-- Opening slide -->
  <section class="slide slide--hero">
    <svg class="shapes" width="536" height="301" viewBox="0 0 536 301">
      <defs>
        <linearGradient id="heroPhoto" x1="0" y1="0" x2="1" y2="1">
          <stop offset="0" stop-color="#4fb2ea"/>
          <stop offset=".5" stop-color="#a9dcf6"/>
          <stop offset="1" stop-color="#5aa8e3"/>
        </linearGradient>
      </defs>
      <polygon points="0,0 345,0 173,301 0,301" fill="url(#heroPhoto)" role="img" aria-label="Professional holding a tablet beneath a glowing network globe of digital icons"/>
      <polygon points="345,0 518,301 173,301" fill="var(--blue)"/>
      <polygon points="210,301 330,240 470,301" fill="var(--blue-soft)" opacity=".8"/>
    </svg>
    <div class="brand brand--large" style="left:393px;top:14px;">NOVA<small>Consulting Group</small></div>
    <p class="abs headline" style="left:270px;top:134px;">Everyone Talks about<br>Cloud &amp; Digital<br>Transformation</p>
    <span class="rule" style="left:270px;top:191px;width:49px;"></span>
    <p class="abs strong-line" style="left:272px;top:200px;">We do it differently</p>
  </section>

  <!-- Cover slide -->
  <section class="slide slide--cover">
    <svg class="shapes" width="536" height="301" viewBox="0 0 536 301">
      <defs>
        <linearGradient id="coverPhoto" x1="0" y1="0" x2="1" y2="1">
          <stop offset="0" stop-color="#0d2747"/>
          <stop offset=".55" stop-color="#1e4f86"/>
          <stop offset="1" stop-color="#d9dde4"/>
        </linearGradient>
      </defs>
      <polygon points="198,0 536,0 536,301 370,301" fill="url(#coverPhoto)" role="img" aria-label="Young professional with a lanyard reading a tablet in a server room"/>
      <polygon points="192,0 370,301 21,301" fill="var(--blue)"/>
      <polygon points="70,301 180,235 330,301" fill="var(--blue-soft)" opacity=".8"/>
    </svg>
    <div class="brand brand--large" style="left:33px;top:15px;">NOVA<small>Consulting Group</small></div>
    <p class="abs headline" style="left:121px;top:131px;font-size:16px;line-height:1.15;">Consulting<br>Services<br>Offerings</p>
    <span class="rule" style="left:123px;top:191px;width:48px;"></span>
    <p class="abs strong-line" style="left:123px;top:199px;">12 Dec 2025</p>
  </section>

  <!-- Discussion topics -->
  <section class="slide slide--topics">
    <svg class="shapes" width="536" height="301" viewBox="0 0 536 301">
      <defs>
        <linearGradient id="topicsPhoto" x1="0" y1="0" x2="0" y2="1">
          <stop offset="0" stop-color="var(--orange)"/>
          <stop offset=".55" stop-color="#c98a6a"/>
          <stop offset="1" stop-color="#e9e9ee"/>
        </linearGradient>
      </defs>
      <rect x="269" y="0" width="267" height="301" fill="url(#topicsPhoto)" role="img" aria-label="Businesswoman reviewing charts on a tablet in a bright office"/>
    </svg>
    <h2 class="slide-title">DISCUSSION TOPICS</h2>
    <div class="topic" style="left:114px;top:97px;"><span class="topic-icon"></span>Branding</div>
    <div class="topic" style="left:229px;top:107px;"><span class="topic-icon"></span>Offerings</div>
    <div class="topic" style="left:342px;top:97px;"><span class="topic-icon"></span>Competitor<br>Market</div>
    <div class="topic" style="left:54px;top:174px;"><span class="topic-icon"></span>Organizational<br>Structure</div>
    <div class="topic" style="left:175px;top:174px;"><span class="topic-icon"></span>People<br>Development</div>
    <div class="topic" style="left:290px;top:174px;"><span class="topic-icon"></span>Timeline</div>
    <div class="topic" style="left:402px;top:174px;"><span class="topic-icon"></span>Budget</div>
    <div class="brand brand--small" style="left:480px;top:272px;">NOVA<small>Consulting Group</small></div>
  </section>

  <!-- Focus timeline -->
  <section class="slide slide--focus">
    <svg class="shapes" width="536" height="301" viewBox="0 0 536 301">
      <polygon points="235,150 536,150 536,259 175,259" fill="var(--panel-grey)"/>
      <polygon points="0,240 34,301 0,301" fill="var(--blue)"/>
      <line x1="44" y1="78" x2="253" y2="78" stroke="var(--line-grey)" stroke-width="2"/>
      <line x1="255" y1="170" x2="464" y2="170" stroke="var(--line-grey)" stroke-width="2"/>
      <g fill="var(--blue)">
        <circle cx="44" cy="78" r="13"/><circle cx="149" cy="78" r="13"/><circle cx="253" cy="78" r="13"/>
        <circle cx="255" cy="170" r="13"/><circle cx="361" cy="170" r="13"/><circle cx="464" cy="170" r="13"/>
      </g>
      <g fill="none" stroke="var(--white)" stroke-width="2" stroke-linecap="round" stroke-linejoin="round">
        <path d="M38 78 l4 4 l8 -8"/><path d="M143 78 l4 4 l8 -8"/><path d="M247 78 l4 4 l8 -8"/>
        <path d="M249 170 l4 4 l8 -8"/><path d="M355 170 l4 4 l8 -8"/><path d="M458 170 l4 4 l8 -8"/>
      </g>
    </svg>
    <h2 class="slide-title">PUBLIC CLOUD IS OUR FOCUS</h2>
    <p class="point" style="left:26px;top:102px;">All NOVA’s Services encompasses Public Cloud KRT</p>
    <p class="point" style="left:132px;top:101px;">We focus on the journey to achieve digital transformation on the cloud</p>
    <p class="point" style="left:236px;top:102px;">KRT Suite Public Cloud is the central backbone</p>
    <p class="point" style="left:236px;top:197px;">Our focus is on APAC and EMEA</p>
    <p class="point" style="left:344px;top:197px;">Our free assessments provide insights into your key challenges to move to the cloud</p>
    <p class="point" style="left:447px;top:197px;">We transform your business processes to standardize on core KRT</p>
    <div class="brand brand--small" style="left:482px;top:272px;">NOVA<small>Consulting Group</small></div>
  </section>

  <!-- Services -->
  <section class="slide slide--services">
    <svg class="shapes" width="536" height="301" viewBox="0 0 536 301">
      <polygon points="269,36 392,250 148,250" fill="var(--pale-tri)"/>
      <polygon points="269,127 340,250 198,250" fill="var(--blue-pale)" opacity=".45"/>
      <g stroke="var(--white)" stroke-width="1">
        <line x1="223" y1="61" x2="236" y2="61"/><line x1="300" y1="61" x2="313" y2="61"/>
        <line x1="195" y1="109" x2="208" y2="109"/><line x1="336" y1="109" x2="349" y2="109"/>
        <line x1="171" y1="151" x2="184" y2="151"/><line x1="359" y1="151" x2="372" y2="151"/>
        <line x1="145" y1="195" x2="158" y2="195"/>
      </g>
      <g fill="#4b5c92" stroke="var(--white)" stroke-width="1.2">
        <circle cx="255" cy="61" r="9"/><circle cx="287" cy="61" r="9"/>
        <circle cx="228" cy="109" r="9"/><circle cx="311" cy="109" r="9"/>
        <circle cx="205" cy="151" r="9"/><circle cx="333" cy="151" r="9"/>
        <circle cx="179" cy="195" r="9"/>
      </g>
      <path d="M201 151 l3 3 l5 -6" fill="none" stroke="var(--white)" stroke-width="1.4"/>
    </svg>
    <h2 class="slide-title">CLOUD ASSESSMENTS &amp; ADVISORY SERVICES</h2>
    <p class="service service--left" style="right:328px;top:50px;">Business<br>Transformation</p>
    <p class="service service--left" style="right:352px;top:100px;">Architecture &amp;<br>Transition State</p>
    <p class="service service--left" style="right:376px;top:141px;">Data Strategy &amp;<br>Governance</p>
    <p class="service service--left" style="right:397px;top:186px;">Operational<br>Stability</p>
    <p class="service" style="left:338px;top:50px;">ROI<br>Realization</p>
    <p class="service" style="left:360px;top:100px;">Design<br>Authority</p>
    <p class="service" style="left:381px;top:141px;">Operational Stability<br>&amp; Efficiencency</p>
    <span class="pill"></span>
    <div class="brand brand--small" style="left:482px;top:272px;">NOVA<small>Consulting Group</small></div>
  </section>

</main>
</body>
</html>
```